Business Card Design and Logo Needed

I need Business Cards and a Logo for my website and public speaking business which can be found at: www.kelsa-thorn.example

I'm looking for creative and unique ideas. Some business cards I've found online that I like can be found at:
http://gigplatelo.example/general/18-smokin-hot-business-card-designs/

and at

http://www.vortaplume.example/2009/04/50-creative-business-cards-of-50-graphic-designers/

```html
<!DOCTYPE html>
<html lang="en">
<head>
<meta charset="utf-8">
<title>Kelsa Thorn — Business Card</title>
<link rel="stylesheet" href="https://fonts.googleapis.com/css2?family=Sacramento&family=Russo+One&display=swap">
<style>
  :root {
    --page: #ffffff;
    --card: #2b0d09;
    --tan: #d8b88c;
    --ornament-light: #8a6a52;
    --ornament-dark: #5a3a2c;
  }
  html, body {
    margin: 0;
    width: 1200px;
    height: 900px;
    overflow: hidden;
    background: var(--page);
  }
  .card {
    position: absolute;
    left: 10px;
    top: 126px;
    width: 1180px;
    height: 654px;
    background: var(--card);
    overflow: hidden;
  }
  .damask-frame {
    position: absolute;
    inset: 0;
    width: 1180px;
    height: 654px;
  }
  .card-content {
    position: absolute;
    left: 190px;
    top: 154px;
    width: 800px;
    height: 316px;
    text-align: center;
    color: var(--tan);
  }
  .name {
    margin: 0;
    padding-top: 40px;
    font-family: "Sacramento", cursive;
    font-weight: 400;
    font-size: 124px;
    line-height: 120px;
    letter-spacing: 4px;
  }
  .roles {
    margin: 10px 0 0;
    font-family: "Russo One", sans-serif;
    font-size: 18px;
    letter-spacing: 2.5px;
    text-transform: uppercase;
  }
  .contact {
    margin: 56px 0 0;
    font-family: "Russo One", sans-serif;
    font-size: 14px;
    letter-spacing: 1.2px;
    text-transform: uppercase;
    white-space: nowrap;
  }
  .contact .sep { padding: 0 6px; }
</style>
</head>
<body>
  <div class="card">
    <svg class="damask-frame" viewBox="0 0 1180 654" role="img" aria-label="Tan damask floral ornament pattern framing the card on all sides">
      <defs>
        <linearGradient id="damask-tone" x1="0" y1="0" x2="0" y2="1">
          <stop offset="0" stop-color="var(--ornament-light)"/>
          <stop offset="0.5" stop-color="var(--ornament-dark)"/>
          <stop offset="1" stop-color="var(--ornament-light)"/>
        </linearGradient>
      </defs>
      <path fill="url(#damask-tone)" fill-rule="evenodd"
            d="M0 0H1180V654H0Z M190 154H990V470H190Z"/>
    </svg>
    <div class="card-content">
      <h1 class="name">Kelsa Thorn</h1>
      <p class="roles">Speaker, Philanthropist, Author</p>
      <p class="contact">Phone: 07700900418<span class="sep">•</span>E-mail: info@kelsa-thorn.example<span class="sep">•</span>www.kelsa-thorn.example</p>
    </div>
  </div>
</body>
</html>
```